lanternly cider - bottle label, and poster

we need a label designed for a 500ml bottle of cider. The cider will be first of three that will be produced, and will be part of a 3 bottle pack. The first cider is a ginger cider, giving the full flavour of the ginger without the heat. Our first thought was the label could be based upon a wanted poster, other than that we are open to ideas.

Target Market(s)

young mid 20's and hipsters, and cider drinkers of course!

Industry/Entity Type

Brewery

Font styles to use
Serif
Other font styles liked:
• 'the copper meadow'

Requirements
Must have
• 500ml 4.5% ABV, allow area for brand discripton, and bottle story (to be added later).
Nice to have
• wanted poster style

```html
<!DOCTYPE html>
<html lang="en">
<head>
<meta charset="utf-8">
<title>Lanternly Cider – Ginger Cider Label</title>
<link rel="stylesheet" href="https://fonts.googleapis.com/css2?family=Smokum&family=Rye&family=Oswald:wght@500;600&display=swap">
<style>
  :root {
    --page: #ffffff;
    --ink: #46351f;
    --parchment-light: #efe4cb;
    --parchment-mid: #e2d0ad;
    --parchment-edge: #b98c57;
    --ginger-light: #d9c7a4;
    --ginger-dark: #4a3a26;
    --hole: #1f1a16;
    --hole-rim: #8c8f96;
  }
  * { margin: 0; padding: 0; box-sizing: border-box; }
  html, body {
    width: 1200px; height: 875px; overflow: hidden;
    background: var(--page);
  }
  .canvas { position: relative; width: 1200px; height: 875px; }
  .label {
    position: absolute; left: 320px; top: 44px;
    width: 560px; height: 786px;
    overflow: hidden;
    background:
      radial-gradient(ellipse at 50% 45%, var(--parchment-light) 0%, var(--parchment-mid) 55%, var(--parchment-edge) 100%);
    color: var(--ink);
  }
  .rule {
    position: absolute; left: 56px; width: 448px; height: 8px;
    background: var(--ink);
  }
  .rule--top { top: 52px; }
  .rule--bottom { top: 192px; }
  .title-band {
    position: absolute; left: 0; top: 62px; width: 100%; height: 128px;
    display: flex; align-items: center; justify-content: center;
  }
  .title {
    display: inline-block;
    white-space: nowrap;
    font-family: "Smokum", "Rye", serif;
    font-weight: 400;
    font-size: 125px; line-height: 128px;
    letter-spacing: 2px;
    transform: scaleX(0.4);
    transform-origin: center center;
  }
  .bullet-hole {
    position: absolute; width: 30px; height: 30px; border-radius: 50%;
    background: radial-gradient(circle, var(--hole) 0 55%, var(--hole-rim) 56% 100%);
  }
  .bullet-hole--title { left: 497px; top: 147px; }
  .bullet-hole--art { left: 146px; top: 372px; }
  .ginger-art {
    position: absolute; left: 160px; top: 224px; width: 240px; height: 172px;
    border-radius: 40% 50% 45% 55%;
    background: radial-gradient(ellipse at 50% 50%, var(--ginger-light) 0%, var(--ginger-dark) 100%);
  }
  .spec {
    position: absolute; top: 291px; width: 108px; height: 45px;
    border-top: 3px solid var(--ink); border-bottom: 3px solid var(--ink);
    display: flex; align-items: center; justify-content: center;
    font-family: "Oswald", sans-serif; font-weight: 600;
    font-size: 24px; letter-spacing: 0.5px;
  }
  .spec--volume { left: 35px; }
  .spec--abv { left: 418px; }
  .tagline {
    position: absolute; left: 0; top: 434px; width: 100%;
    text-align: center;
    font-family: "Rye", serif;
    font-size: 27px; line-height: 45px;
  }
  .stars {
    position: absolute; left: 0; top: 537px; width: 100%;
    display: flex; justify-content: center; align-items: center; gap: 16px;
  }
  .star { fill: var(--ink); }
</style>
</head>
<body>
<main class="canvas">
  <section class="label" aria-label="Lanternly Cider ginger cider bottle label">
    <div class="rule rule--top"></div>
    <div class="title-band"><h1 class="title">GINGER CIDER</h1></div>
    <div class="rule rule--bottom"></div>
    <div class="bullet-hole bullet-hole--title" role="img" aria-label="Bullet hole"></div>

    <div class="spec spec--volume">500ml</div>
    <div class="ginger-art" role="img" aria-label="Engraved illustration of a ginger root"></div>
    <div class="spec spec--abv">4.5% ABV</div>
    <div class="bullet-hole bullet-hole--art" role="img" aria-label="Bullet hole"></div>

    <p class="tagline">FULL FLAVOUR OF THE GINGER<br>WITHOUT THE HEAT</p>

    <div class="stars" aria-hidden="true">
      <svg width="39" height="39" viewBox="0 0 100 100"><polygon class="star" points="50,2 61,37 98,37 68,59 79,95 50,73 21,95 32,59 2,37 39,37"/></svg>
      <svg width="64" height="64" viewBox="0 0 100 100"><polygon class="star" points="50,2 61,37 98,37 68,59 79,95 50,73 21,95 32,59 2,37 39,37"/></svg>
      <svg width="39" height="39" viewBox="0 0 100 100"><polygon class="star" points="50,2 61,37 98,37 68,59 79,95 50,73 21,95 32,59 2,37 39,37"/></svg>
    </div>
  </section>
</main>
</body>
</html>
```